Real Estate Development Company Stationary

We need our company, business card, letterhead, pocket folder and envelope designed.

We are a new real estate development company. We focus on data centre, commercial and real estate development.

Please see attached for our logo. Since it's a new logo, you still can make minor adjust if you like it makes senses

The client has sent me a business card he really likes. Please see file 3.

Target Market(s)

Real Estate Investors
Large corporations
Home buyers

Industry/Entity Type

Real Estate

```html
<!DOCTYPE html>
<html lang="en">
<head>
<meta charset="utf-8">
<title>Vantor Development Inc. – Letterhead &amp; Business Cards</title>
<link rel="stylesheet" href="https://fonts.googleapis.com/css2?family=Open+Sans:ital,wght@0,400;0,600;0,700;1,400&display=swap">
<style>
  :root {
    --navy: #0c3f86;
    --green: #5cb531;
    --green-mid: #4f9a6a;
    --sky: #2a8fd0;
    --ink: #2b2b2b;
    --muted: #666a70;
    --paper: #ffffff;
    --card-edge: #e3e6ea;
    --card-edge-dark: #cfd3d8;
    --brand-pale: #c9d6ea;
    --backdrop: #3b3c3f;
  }
  * { box-sizing: border-box; margin: 0; padding: 0; }
  html, body {
    width: 1200px; height: 1000px; overflow: hidden;
    background: var(--backdrop);
    font-family: "Open Sans", Arial, sans-serif;
    color: var(--ink);
  }
  .stationery { position: relative; width: 1200px; height: 1000px; }

  /* Letterhead */
  .letterhead {
    position: absolute; left: 60px; top: 60px;
    width: 660px; height: 854px;
    background: var(--paper);
    box-shadow: 0 10px 30px rgba(0,0,0,.35);
    overflow: hidden;
  }
  .letterhead__header {
    position: absolute; top: 44px; left: 56px; right: 56px;
    display: flex; justify-content: space-between; align-items: flex-start;
  }
  .letterhead__contact { font-size: 10px; line-height: 1.5; color: var(--muted); }
  .letterhead__contact .label { color: var(--sky); font-weight: 600; }
  .letterhead__contact .web { color: var(--sky); }
  .brand {
    display: flex; align-items: center; gap: 10px;
    color: var(--green); font-weight: 600; white-space: nowrap;
  }
  .brand__dot { width: 14px; height: 14px; border-radius: 50%; background: var(--navy); flex: none; }
  .letterhead .brand { font-size: 22px; margin-top: 10px; }

  .letterhead__body {
    position: absolute; top: 150px; left: 56px; right: 70px;
    font-size: 12px; line-height: 1.55;
  }
  .recipient { margin-bottom: 16px; }
  .letter-title { font-weight: 700; font-size: 11px; text-transform: uppercase; margin-bottom: 14px; }
  .letter-text p { margin-bottom: 12px; }
  .letter-list { padding-left: 26px; margin-bottom: 14px; }
  .letter-list li { margin-bottom: 12px; padding-left: 6px; }
  .signoff { margin-top: 18px; }
  .signoff .signer { font-weight: 700; margin-top: 18px; }

  .letterhead__footer {
    position: absolute; left: 0; right: 0; bottom: 0; height: 78px;
    background: var(--navy);
  }
  .footer-accent {
    position: absolute; left: 0; bottom: 50px; width: 62px; height: 62px;
  }
  .slogan {
    position: absolute; right: 40px; bottom: 28px;
    color: #fff; font-size: 13px;
  }

  /* Business cards */
  .card {
    position: absolute; left: 770px;
    width: 380px; height: 217px;
    box-shadow: 0 4px 0 var(--card-edge), 0 8px 0 var(--card-edge-dark), 0 14px 24px rgba(0,0,0,.4);
  }
  .card--back {
    top: 150px; background: var(--navy);
    display: flex; align-items: center; justify-content: center;
  }
  .card--back .brand { color: var(--brand-pale); font-size: 22px; }
  .card--back .brand__dot { background: var(--brand-pale); width: 16px; height: 16px; }

  .card--front { top: 520px; background: var(--paper); padding: 22px 24px; }
  .card__name { font-size: 14px; font-weight: 700; color: var(--ink); }
  .card__role { font-size: 10px; color: var(--sky); }
  .card--front .brand { position: absolute; right: 26px; top: 86px; font-size: 18px; }
  .card__contact {
    position: absolute; right: 26px; bottom: 18px;
    text-align: right; font-size: 9.5px; line-height: 1.5; color: var(--muted);
  }
  .card__contact .label { color: var(--sky); font-weight: 600; }
  .card__contact .web { color: var(--sky); font-weight: 600; }
</style>
</head>
<body>
<main class="stationery">

  <section class="letterhead" aria-label="Letterhead">
    <header class="letterhead__header">
      <div class="letterhead__contact">
        <div>Address here, City, State, Zip Code</div>
        <div><span class="label">T</span> 555-010-4417</div>
        <div><span class="label">E</span> mira.olsen@vantordev.ca</div>
        <div class="web">www.vantordev.ca</div>
      </div>
      <div class="brand"><span class="brand__dot"></span>Vantor Development Inc.</div>
    </header>

    <div class="letterhead__body">
      <div class="recipient">
        Recipient Name<br>Address Line 1<br>Address Line 2<br>City, State, Zip Code
      </div>
      <div class="letter-title">Title Here</div>
      <div class="letter-text">
        <p>These are sample text only. These are sample text only. These are sample text only. These are sample text only. These are sample text only. These are sample text only.</p>
        <ol class="letter-list" start="2">
          <li>These are sample text only. These are sample text only. These are sample text only. These are sample text only. These are sample text only. These are sample text only. These are sample text only.</li>
          <li>These are sample text only. These are sample text only. These are sample text only. These are sample text only. These are sample text only. These are sample text only.</li>
        </ol>
      </div>
      <div class="signoff">
        Warm Regards,
        <div class="signer">Mira Olsen</div>
      </div>
    </div>

    <footer class="letterhead__footer">
      <svg class="footer-accent" viewBox="0 0 62 62" aria-hidden="true">
        <rect x="0" y="0" width="62" height="38" fill="#5cb531"/>
        <rect x="0" y="38" width="62" height="24" fill="#4f9a6a"/>
      </svg>
      <div class="slogan">Slogan Goes Here</div>
    </footer>
  </section>

  <section class="card card--back" aria-label="Business card back">
    <div class="brand"><span class="brand__dot"></span>Vantor Development Inc.</div>
  </section>

  <section class="card card--front" aria-label="Business card front">
    <div class="card__name">Mira Olsen</div>
    <div class="card__role">Project Manager</div>
    <div class="brand"><span class="brand__dot"></span>Vantor Development Inc.</div>
    <div class="card__contact">
      <div>Address here, City, State, Zip Code</div>
      <div><span class="label">T</span> 555-010-4417 &nbsp;<span class="label">C</span> 555-010-6032</div>
      <div><span class="label">E</span> mira.olsen@vantordev.ca</div>
      <div class="web">www.vantordev.ca</div>
    </div>
  </section>

</main>
</body>
</html>
```